Sports Psychology Business Card Design

Need a catchy and unique business card design for our sport psychology practice. We provide mental performance counseling and consulting to performers from all types of industries with a special emphases on athletes.The name of our practice is "Steady Core of Achievement" or "SCA" as is indicated in the logo examples submitted in this brief. Also provided were logos with specific sports referenced which represent sources of our clients from those sports.

Target Market(s)

Executives, Professionals (doctors, lawyers, etc.), Athletes, Entertainers and other performers

Contact Information for Business Card

Need to include our logo (logos provided in this brief).

Font styles to use
Other font styles liked:
• Font can be found in logo

Colors
0792cd
34a7d8
85cae6

Requirements
Must have
• Our logo and reference to our provision of mental performance counseling/consulting/coaching
Nice to have
• References to sports that our athletes play as provided in the brief.
Should not have
• This is not a general wellness consulting practice. Our focus is on consulting to improve mental performance.

```html
<!DOCTYPE html>
<html lang="en">
<head>
<meta charset="utf-8">
<title>Steady Core of Achievement — Business Card</title>
<link rel="stylesheet" href="https://fonts.googleapis.com/css2?family=Open+Sans:wght@400;600;700&display=swap">
<style>
  :root {
    --canvas: #e4e5e7;
    --card-dark: #1c1e21;
    --card-light: #ffffff;
    --accent: #0a6fc7;
    --ink-light: #f2f2f2;
    --ink-soft: #bfc3c8;
  }
  * { margin: 0; padding: 0; box-sizing: border-box; }
  html, body {
    width: 1200px; height: 1000px; overflow: hidden;
    background: var(--canvas);
    font-family: "Open Sans", Arial, sans-serif;
  }
  .sheet {
    width: 1200px; height: 1000px;
    display: flex; flex-direction: column;
    align-items: center; justify-content: center; gap: 56px;
  }
  .card {
    position: relative; width: 640px; height: 366px; overflow: hidden;
    box-shadow: 0 6px 18px rgba(0,0,0,0.12);
  }
  .card--front {
    background: linear-gradient(135deg, #17191b 0%, #2a2d31 100%);
    display: flex; align-items: center; justify-content: center;
  }
  .brand {
    display: flex; align-items: center; gap: 14px;
    font-weight: 700; letter-spacing: 6px; line-height: 1;
  }
  .brand__dot { width: 18px; height: 18px; border-radius: 50%; background: var(--accent); }
  .card--front .brand { color: var(--card-light); font-size: 78px; }
  .card--back { background: var(--card-light); }
  .card__wave { position: absolute; inset: 0; width: 100%; height: 100%; }
  .card--back .brand {
    position: absolute; left: 330px; top: 92px;
    color: var(--card-dark); font-size: 62px;
  }
  .identity { position: absolute; left: 26px; top: 184px; color: var(--ink-light); }
  .identity__name { font-size: 22px; font-weight: 600; line-height: 28px; }
  .identity__role { font-size: 12px; color: var(--ink-soft); margin-top: 0; }
  .contact {
    position: absolute; left: 440px; top: 258px;
    color: var(--ink-light); font-size: 13px; line-height: 19px; list-style: none;
  }
  .contact__item { display: flex; align-items: center; gap: 8px; }
  .contact__item--plain { padding-left: 20px; }
  .contact__icon { width: 12px; height: 12px; flex: none; }
</style>
</head>
<body>
<main class="sheet">
  <section class="card card--front" aria-label="Card front">
    <div class="brand"><span class="brand__dot"></span><span>SCA</span></div>
  </section>

  <section class="card card--back" aria-label="Card back">
    <svg class="card__wave" viewBox="0 0 640 366" preserveAspectRatio="none" aria-hidden="true">
      <path d="M40,0 C110,150 180,235 330,258 C430,258 530,200 640,180 L640,366 L0,366 L0,0 Z" fill="var(--card-dark)"/>
      <path d="M54,0 C124,146 192,228 330,250" fill="none" stroke="var(--accent)" stroke-width="6"/>
    </svg>
    <div class="brand"><span class="brand__dot"></span><span>SCA</span></div>
    <div class="identity">
      <p class="identity__name">Name Title</p>
      <p class="identity__role">designation</p>
    </div>
    <ul class="contact">
      <li class="contact__item contact__item--plain">suit # 00, Lorem ipsum</li>
      <li class="contact__item contact__item--plain">Lorem Lorem ipsum</li>
      <li class="contact__item">
        <svg class="contact__icon" viewBox="0 0 12 12"><path d="M2.5 1h2l1 3-1.3 1a6 6 0 0 0 2.8 2.8L8 6.5l3 1v2A1.5 1.5 0 0 1 9.5 11 8.5 8.5 0 0 1 1 2.5 1.5 1.5 0 0 1 2.5 1z" fill="currentColor"/></svg>
        <span>000-000-0000</span>
      </li>
      <li class="contact__item">
        <svg class="contact__icon" viewBox="0 0 12 12"><rect x="0.5" y="2" width="11" height="8" fill="currentColor"/><path d="M0.5 2 6 6.5 11.5 2" fill="none" stroke="var(--card-dark)" stroke-width="1"/></svg>
        <span>hello@lmarlow.com</span>
      </li>
      <li class="contact__item">
        <svg class="contact__icon" viewBox="0 0 12 12" fill="none" stroke="currentColor" stroke-width="1"><circle cx="6" cy="6" r="5"/><ellipse cx="6" cy="6" rx="2.2" ry="5"/><path d="M1 6h10"/></svg>
        <span>www.lmarlow.com</span>
      </li>
    </ul>
  </section>
</main>
</body>
</html>
```